Branvique needs a business Card Design

We are looking for a business card Design for our new Managed Service Provider Company, Branvique. Branvique encompasses everything IT for the average medium sized business. Our primary services are help desk support, cyber-security (malware and ransomware protection), and Disaster Recovery systems. We would like the design to have a very clean and professional look, with a very minimalist feel.

Target Market(s)

Medium to large sized businesses

Industry/Entity Type

It Service

Contact Information for Business Card

Name GoesHere
name@branvique.com
O: 555-382-6047
C: 555-731-5820

Font styles to use
Other font styles liked:
• Poppins Font Only Please

Colors

Designer to choose only greyscale colors for use in the design.

Requirements
Must have
• Logo included
Nice to have
• Cutting Edge, innovative, minimalistic, elegant

```html
<!DOCTYPE html>
<html lang="en">
<head>
<meta charset="utf-8">
<title>Branvique Business Card</title>
<link href="https://fonts.googleapis.com/css2?family=Poppins:wght@400;500&display=swap" rel="stylesheet">
<style>
  :root {
    --page-bg: #e6e6e6;
    --front-deep: #111111;
    --front-mid: #2b2b2b;
    --front-glow: #4a4a4a;
    --circuit-grey: rgba(190, 190, 190, 0.28);
    --wash-grey: rgba(150, 150, 150, 0.22);
    --wordmark-white: #ffffff;
    --web-grey: #cfcfcf;
    --ink-charcoal: #1e1e1e;
    --mark-grey: #2a2a2a;
    --card-white: #ffffff;
  }
  * { margin: 0; padding: 0; box-sizing: border-box; }
  html, body {
    width: 933px;
    height: 1200px;
    overflow: hidden;
  }
  body {
    background: var(--page-bg);
    font-family: "Poppins", sans-serif;
    position: relative;
  }
  .card {
    position: absolute;
    left: 136px;
    width: 667px;
    height: 380px;
    overflow: hidden;
    box-shadow: 0 10px 22px rgba(0, 0, 0, 0.28);
  }

  /* Front */
  .card-front {
    top: 109px;
    background: radial-gradient(ellipse at 50% 45%, var(--front-glow) 0%, var(--front-mid) 32%, var(--front-deep) 80%);
  }
  .circuit-field {
    position: absolute;
    top: 0;
    height: 100%;
    width: 190px;
  }
  .circuit-field--left {
    left: 0;
    background: linear-gradient(90deg, var(--circuit-grey), rgba(190, 190, 190, 0));
  }
  .circuit-field--right {
    right: 0;
    background: linear-gradient(270deg, var(--circuit-grey), rgba(190, 190, 190, 0));
  }
  .front-mark {
    position: absolute;
    left: 311px;
    top: 142px;
    width: 44px;
    height: 44px;
    background: var(--wordmark-white);
  }
  .front-wordmark {
    position: absolute;
    left: 0;
    right: 0;
    top: 236px;
    text-align: center;
    color: var(--wordmark-white);
    font-weight: 400;
    font-size: 30px;
    letter-spacing: 13px;
    text-indent: 13px;
    line-height: 1;
  }
  .front-website {
    position: absolute;
    left: 0;
    right: 0;
    top: 330px;
    text-align: center;
    color: var(--web-grey);
    font-weight: 400;
    font-size: 23px;
    line-height: 1;
  }

  /* Back */
  .card-back {
    top: 711px;
    background: var(--card-white);
  }
  .circuit-wash {
    position: absolute;
    inset: 0;
    background: linear-gradient(180deg, var(--wash-grey) 0%, rgba(150, 150, 150, 0.1) 55%, rgba(150, 150, 150, 0.03) 100%);
  }
  .back-mark {
    position: absolute;
    left: 36px;
    top: 88px;
    width: 150px;
    height: 150px;
    background: var(--mark-grey);
  }
  .back-wordmark {
    position: absolute;
    left: 24px;
    top: 340px;
    color: var(--ink-charcoal);
    font-weight: 500;
    font-size: 18px;
    letter-spacing: 6px;
    line-height: 1;
  }
  .contact {
    position: absolute;
    left: 255px;
    top: 96px;
    list-style: none;
    color: var(--ink-charcoal);
    font-weight: 400;
    font-size: 33px;
    line-height: 44px;
    text-shadow: 0 0 4px rgba(255, 255, 255, 0.9), 0 1px 3px rgba(30, 30, 30, 0.35);
  }
</style>
</head>
<body>
  <section class="card card-front">
    <div class="circuit-field circuit-field--left" role="img" aria-label="Circuit-board line pattern"></div>
    <div class="circuit-field circuit-field--right" role="img" aria-label="Circuit-board line pattern"></div>
    <div class="front-mark"></div>
    <div class="front-wordmark">BRANVIQUE</div>
    <div class="front-website">www.branvique.com</div>
  </section>

  <section class="card card-back">
    <div class="circuit-wash" role="img" aria-label="Light circuit-board line pattern"></div>
    <div class="back-mark"></div>
    <div class="back-wordmark">BRANVIQUE</div>
    <ul class="contact">
      <li class="contact-name">Name GoesHere</li>
      <li class="contact-email">name@branvique.com</li>
      <li class="contact-office">O: 555-382-6047</li>
      <li class="contact-cell">C: 555-731-5820</li>
    </ul>
  </section>
</body>
</html>
```